Norvale Code Builders Summit

We need a web design for a new brand of annual software development conference hosted in Riga, Latvia. Previously we used this page http://brimtorfest.lv/ and we also have a small concept over here http://www.brimtorfest.tk/. It is possible to view the content from past years there. It will not change radically next year.

Due to organisational changes we are rebranding the conference to 'Tolvik Code Meet' therefore we need a new web site and logo. Logo could be just 'TOLVIK CODE MEET' letters with proper font and font color selected, but if you like you could go creative. We also have a mobile app, which will be branded according to the designed web site afterwards. This is purely software development conference, so the web site visitors are techies. It will contain standard conference information such as schedule, speakers info, announcements, photos etc. The intention of this project is to create a design, which would attract people by ensuring that content quality would be on a high level.

The design should be modern, simple and without clutter. The design is intended to be responsive. The entry location should make accent on the conference date (22 of January, 2015) and some kind of short slogan (5-6 words max). Page should have initial wow effect for technical geeks.

Conference is organised by several local user groups (PKO Latvia, WMB Riga, TRZAP). Logos are attached. These are organisers, not sponsors.

One of the examples of something similar to what we would like to have http://www.quorvenfest.org/
Updates

Payment is now guaranteed in this project.

Target Market(s)

Software developers

Industry/Entity Type

Software

Requirements
Must have
• Should say TOLVIK CODE MEET as a main title.
Modern looking.
Shows conference speakers with their photos.
Presents conference schedule in 4-5 parallel tracks.
Place to put organisers an sponsors logos.
Social network promotion buttons.
Nice to have
• Parallax scrolling design.
Nice background using photos from previous events (https://pics.velmorashare.com/photos/+oswintharle/albums/7392018465527104816, https://pics.velmorashare.com/u/1/photos/302957184620473918264/albums/8163027594410273925)
Integrated Chirplex feed.
Should not have
• Photos of unrelated people.
Cliche photos and pictures.
Orange color as main one.

```html
<!DOCTYPE html>
<html lang="en">
<head>
<meta charset="utf-8">
<title>Tolvik Code Meet</title>
<link href="https://fonts.googleapis.com/css2?family=Oswald:wght@400;500;700&family=Raleway:wght@400;500;600;700&display=swap" rel="stylesheet">
<style>
:root{
  --blue:#0e77a8;
  --blue-deep:#0b6791;
  --band:#2f6687;
  --band-dark:#28597a;
  --contact:#3b6d8a;
  --grey-bar:#f1f1f1;
  --text:#6b6b6b;
  --muted:#9a9a9a;
  --white:#ffffff;
  --line:#d6d6d6;
}
*{box-sizing:border-box;margin:0;padding:0}
html,body{width:1200px;height:2358px;overflow:hidden}
body{position:relative;background:var(--white);font-family:"Raleway",Arial,sans-serif;color:var(--text)}
.abs{position:absolute}

/* header */
.topbar{left:0;top:0;width:1200px;height:77px;background:var(--grey-bar);border-top:3px solid var(--blue)}
.nav{left:187px;top:21px;display:flex;font-family:"Oswald",Arial,sans-serif;font-size:14px;color:#333;text-transform:uppercase}
.nav a{color:#333;text-decoration:none;display:block;height:33px;line-height:31px;padding:0 9px;margin-right:5px;letter-spacing:.3px}
.nav a.active{border:2px solid var(--blue);color:var(--blue);border-radius:2px}
.nav .caret{font-size:9px;margin-left:4px}
.share{top:29px;display:flex;align-items:center;gap:3px;font-size:9px}
.share .btn{background:#e9eef3;border:1px solid #c7d0da;border-radius:2px;padding:1px 5px;color:#333;font-weight:700}
.share .count{border:1px solid #ccc;background:#fff;padding:1px 4px;border-radius:2px;color:#666}

/* hero */
.hero-photo{left:0;top:77px;width:1200px;height:398px;background:linear-gradient(90deg,#8c8f93 0%,#cfd3d8 25%,#e9e4e1 55%,#d8cfd6 80%,#c7c4cb 100%)}
.hero-band{left:0;top:77px;width:1200px;height:124px;background:rgba(14,130,190,.88)}
.hero-title{left:187px;top:92px;font-family:"Oswald",Arial,sans-serif;font-weight:700;font-size:44px;line-height:52px;color:var(--white);letter-spacing:1px;white-space:nowrap}
.hero-date{left:187px;top:154px;font-weight:600;font-size:22px;line-height:26px;color:var(--white);letter-spacing:.5px}
.hero-copy{left:584px;top:92px;width:430px}
.hero-text{font-size:12.5px;line-height:20px;color:var(--white);font-weight:500}
.hero-more{display:inline-block;margin-top:4px;font-size:13px;font-weight:700;color:var(--white);text-decoration:underline;letter-spacing:.5px}
.dots{left:544px;top:441px;display:flex;gap:6px}
.dots span{width:16px;height:16px;border-radius:50%;background:var(--blue);border:2px solid #fff}
.dots span.on{background:#fff;border-color:var(--blue)}

/* section titles */
.section-title{left:0;width:1200px;text-align:center;font-size:33px;font-weight:400;color:var(--blue)}
.intro{left:280px;top:551px;width:640px;text-align:center;font-size:13px;line-height:22px;color:var(--text)}

/* speakers */
.speaker{border-radius:50%;border:4px solid #e5e5e5;background:linear-gradient(135deg,#b9a79a,#6f6762)}
.speaker.main{border:5px solid var(--blue);background:linear-gradient(135deg,#d9b79a,#8a7464)}
.arrow{top:672px}
.speaker-name{left:0;top:783px;width:1200px;text-align:center;font-size:29px;color:#444}
.speaker-role{left:0;top:817px;width:1200px;text-align:center;font-size:13px;color:var(--muted)}
.btn-blue{left:513px;top:846px;width:174px;height:32px;background:var(--blue);color:#fff;font-size:13.5px;display:flex;align-items:center;justify-content:center;gap:8px}

/* countdown */
.timeband{left:0;top:975px;width:1200px;height:313px;background:linear-gradient(160deg,var(--band) 0%,#3c7395 50%,var(--band-dark) 100%)}
.badge{width:142px;height:142px;border-radius:50%;background:#fff;display:flex;align-items:center;justify-content:center}
.time-title{left:0;top:1063px;width:1200px;text-align:center;font-size:24px;letter-spacing:1.5px;color:#fff;font-weight:500}
.counter{top:1111px;text-align:center}
.counter .label{font-size:11px;color:#fff;letter-spacing:.8px;height:18px}
.counter .box{height:48px;background:#fff;border:3px solid #d7dde2;font-size:24px;font-weight:500;color:#333;line-height:42px}
.btn-light{left:510px;top:1214px;width:181px;height:32px;background:#fff;color:var(--blue-deep);font-size:13.5px;display:flex;align-items:center;justify-content:center;gap:8px}

/* organisers */
.org-circle{width:116px;height:116px;border-radius:50%;border:2px solid #ececec;background:#fff;display:flex;align-items:center;justify-content:center;font-weight:700;font-size:18px;color:var(--blue-deep)}
.org-name{font-size:17px;font-weight:700;color:var(--blue-deep)}
.org-text{font-size:11.5px;line-height:17px;color:var(--text);width:230px;margin-top:5px}

/* contact */
.contactband{left:0;top:1768px;width:1200px;height:503px;background:linear-gradient(120deg,#3f7190 0%,var(--contact) 45%,#2f6180 100%)}
.contact-title{left:0;top:1848px;width:1200px;text-align:center;font-size:31px;font-weight:400;color:#fff}
.contact-line{left:0;top:1900px;width:1200px;text-align:center;font-size:16.5px;color:#fff;letter-spacing:.3px}
.contact-line .mail{color:#7ecbf0}
.field{background:#fff;border:1px solid #dcdcdc;font-size:14px;color:#555;padding:8px 10px}
.btn-send{left:189px;top:2205px;width:89px;height:33px;background:#fff;color:var(--blue-deep);font-size:14px;display:flex;align-items:center;justify-content:center;gap:8px}

/* footer */
.footer{left:0;top:2271px;width:1200px;height:47px;background:var(--blue)}
.footer-nav{left:187px;top:2286px;display:flex;gap:18px;font-family:"Oswald",Arial,sans-serif;font-size:13px;color:#fff;letter-spacing:.5px}
.footer-social{left:897px;top:2282px;display:flex;gap:6px}
.footer-social span{width:26px;height:26px;border-radius:50%;background:rgba(255,255,255,.45)}
.copyright{left:0;top:2328px;width:1200px;text-align:center;font-size:11px;color:#666}
</style>
</head>
<body>

<header class="abs topbar"></header>
<nav class="abs nav">
  <a class="active" href="#">Home</a><a href="#">Venue</a><a href="#">Speakers</a><a href="#">Schedule</a><a href="#">Talks</a><a href="#">Previous Tolvik Days<span class="caret">▼</span></a>
</nav>
<div class="abs share" style="left:702px"><span class="btn">Chirp</span><span class="count">58</span></div>
<div class="abs share" style="left:786px"><span class="btn">Like</span><span class="count">80</span></div>
<div class="abs share" style="left:870px"><span class="btn">Vote</span><span class="count">34</span></div>
<div class="abs share" style="left:938px"><span class="btn">Share</span><span class="count">36</span></div>

<section>
  <div class="abs hero-photo" role="img" aria-label="Blurred photo of a conference hall with a microphone in the foreground"></div>
  <div class="abs hero-band"></div>
  <h1 class="abs hero-title">TOLVIK CODE MEET</h1>
  <div class="abs hero-date">22 OF JANUARY, 2015</div>
  <div class="abs hero-copy">
    <p class="hero-text">The conference was organised by Latvian Kelvo User Group and Quenmark Systems at November 28th in Riga, Latvia. This was a major Baltics IT event welcoming more than 280 Kelvo programmers from the region.</p>
    <a class="hero-more">READ MORE</a>
  </div>
  <div class="abs dots"><span></span><span></span><span class="on"></span><span></span><span></span></div>
</section>

<section>
  <h2 class="abs section-title" style="top:495px">Our Speakers</h2>
  <p class="abs intro">Lorem ipsum dolor sit amet, consectetur adipiscing elit. Fusce eget mauris vel libero adipiscing condimentum. Vestibulum at auctor lorem, in elementum lorem. Cras suscipit leo at nisl pharetra, eu faucibus dui rhoncus. Integer eros lacus, pretium rutrum erat nec, pulvinar eleifend nisl.</p>
  <svg class="abs arrow" style="left:216px" width="26" height="50" viewBox="0 0 26 50"><polyline points="22,6 6,25 22,44" fill="none" stroke="#0e77a8" stroke-width="4"/></svg>
  <svg class="abs arrow" style="left:958px" width="26" height="50" viewBox="0 0 26 50"><polyline points="4,6 20,25 4,44" fill="none" stroke="#0e77a8" stroke-width="4"/></svg>
  <div class="abs speaker" style="left:271px;top:645px;width:108px;height:108px" role="img" aria-label="Speaker portrait"></div>
  <div class="abs speaker" style="left:402px;top:645px;width:108px;height:108px" role="img" aria-label="Speaker portrait"></div>
  <div class="abs speaker main" style="left:532px;top:631px;width:136px;height:136px" role="img" aria-label="Portrait of featured speaker Aldis Karvenko"></div>
  <svg class="abs" style="left:588px;top:764px" width="24" height="12" viewBox="0 0 24 12"><polygon points="0,0 24,0 12,12" fill="#0e77a8"/></svg>
  <div class="abs speaker" style="left:690px;top:645px;width:108px;height:108px" role="img" aria-label="Speaker portrait"></div>
  <div class="abs speaker" style="left:821px;top:645px;width:108px;height:108px" role="img" aria-label="Speaker portrait"></div>
  <div class="abs speaker-name">Aldis Karvenko</div>
  <div class="abs speaker-role">Quenmark Systems, United Kingdom</div>
  <a class="abs btn-blue">Click to more detail <svg width="14" height="14" viewBox="0 0 14 14"><circle cx="7" cy="7" r="7" fill="#fff"/><polyline points="5.5,4 8.5,7 5.5,10" fill="none" stroke="#0e77a8" stroke-width="2"/></svg></a>
</section>

<section>
  <div class="abs timeband" role="img" aria-label="Blue tinted close-up photo of a calendar with a pushpin"></div>
  <div class="abs badge" style="left:529px;top:904px">
    <svg width="120" height="120" viewBox="0 0 120 120"><circle cx="60" cy="60" r="55" fill="none" stroke="#0b6791" stroke-width="5"/><circle cx="60" cy="60" r="32" fill="none" stroke="#0b6791" stroke-width="6"/><polyline points="60,40 60,62 74,62" fill="none" stroke="#0b6791" stroke-width="6" stroke-linecap="round"/></svg>
  </div>
  <div class="abs time-title">TIME LEFT</div>
  <div class="abs counter" style="left:414px;width:84px"><div class="label">DAYS</div><div class="box">4552</div></div>
  <div class="abs counter" style="left:519px;width:66px"><div class="label">HOURS</div><div class="box">14</div></div>
  <div class="abs counter" style="left:610px;width:75px"><div class="label">MINUTES</div><div class="box">42</div></div>
  <div class="abs counter" style="left:711px;width:75px"><div class="label">SECONDS</div><div class="box">32</div></div>
  <a class="abs btn-light">Click to participate <svg width="14" height="14" viewBox="0 0 14 14"><circle cx="7" cy="7" r="7" fill="#0b6791"/><polyline points="5.5,4 8.5,7 5.5,10" fill="none" stroke="#fff" stroke-width="2"/></svg></a>
</section>

<section>
  <h2 class="abs section-title" style="top:1311px">Our Organisers</h2>
  <svg class="abs" style="left:0;top:1288px" width="1200" height="480" viewBox="0 1288 1200 480">
    <g fill="none" stroke="#d3d3d3" stroke-width="2">
      <polyline points="634,1441 748,1441"/>
      <polyline points="374,1527 374,1555 447,1555"/>
      <polyline points="706,1555 730,1555 730,1581"/>
    </g>
  </svg>
  <div class="abs org-circle" style="left:518px;top:1383px">TRZAP</div>
  <div class="abs org-circle" style="left:447px;top:1500px">WMB</div>
  <div class="abs org-circle" style="left:590px;top:1500px">PKO</div>
  <div class="abs" style="left:763px;top:1402px"><div class="org-name">TRZAP</div><p class="org-text">Lorem ipsum dolor sit amet, consectetur adipiscing elit. Fusce eget mauris vel libero adipiscing condimentum.</p></div>
  <div class="abs" style="left:218px;top:1451px"><div class="org-name">WMB Riga</div><p class="org-text">Lorem ipsum dolor sit amet, consectetur adipiscing elit. Fusce eget mauris vel libero adipiscing condimentum.</p></div>
  <div class="abs" style="left:749px;top:1587px"><div class="org-name">PKO Latvia</div><p class="org-text">Lorem ipsum dolor sit amet, consectetur adipiscing elit. Fusce eget mauris vel libero adipiscing condimentum.</p></div>
</section>

<section>
  <div class="abs contactband" role="img" aria-label="Blue tinted photo of conference attendees talking"></div>
  <div class="abs badge" style="left:529px;top:1697px">
    <svg width="120" height="120" viewBox="0 0 120 120"><circle cx="60" cy="60" r="55" fill="none" stroke="#0b6791" stroke-width="5"/><path d="M44 34c3-3 7-3 9 0l5 8c2 3 1 6-1 8l-3 3c3 6 7 10 13 13l3-3c2-2 5-3 8-1l8 5c3 2 3 6 0 9l-4 4c-4 4-12 3-22-4-11-8-18-17-20-26-1-6 0-10 4-13z" fill="#0b6791"/></svg>
  </div>
  <h2 class="abs contact-title">Contact Us</h2>
  <p class="abs contact-line">If you have a question, please contact Edgars Pellin (<span class="mail">epellin@brimtorfest.lv</span>) or phone 800-555-0142</p>
  <div class="abs field" style="left:189px;top:1946px;width:232px;height:33px">Name</div>
  <div class="abs field" style="left:438px;top:1946px;width:233px;height:33px">Email</div>
  <div class="abs field" style="left:189px;top:1997px;width:823px;height:190px">Message</div>
  <a class="abs btn-send">Send <svg width="14" height="14" viewBox="0 0 14 14"><circle cx="7" cy="7" r="7" fill="#0b6791"/><polyline points="5.5,4 8.5,7 5.5,10" fill="none" stroke="#fff" stroke-width="2"/></svg></a>
</section>

<footer>
  <div class="abs footer"></div>
  <nav class="abs footer-nav"><span>HOME</span><span>VENUE</span><span>SPEAKERS</span><span>SCHEDULE</span><span>TALKS</span></nav>
  <div class="abs footer-social"><span></span><span></span><span></span><span></span></div>
  <p class="abs copyright">© Tolvik Code Meet 2013. All rights resereved</p>
</footer>

</body>
</html>
```